Web Design Project for Quorvel Enterprises

Quorvel Enterprises is a small company with expertise in manufacturing, product development, global sourcing and retail. We provide sales/broker, import/export, private label and product development services to both manufacturers and retailers of food, beverage, health and beauty care and general merchandise. Would like a web site that incorporates images that inspire confidence in the areas of international trade and product development as well as convey the experience of founder and CEO in these areas.

Own web address quorvelenterprises.net and have hosting from brisk nest.com

Target Market(s)

Retail and manufacturing professionals.

Industry/Entity Type

It Company

Font styles to use
Serif
Sans Serif

Requirements
Must have
• Tabs for: Home, About Us, Services, Contact Us

```html
<!DOCTYPE html>
<html lang="en">
<head>
<meta charset="utf-8">
<title>Quorvel Enterprises</title>
<link rel="stylesheet" href="https://fonts.googleapis.com/css2?family=Arimo:wght@400;700&display=swap">
<style>
:root{
  --brand:#1a3d9a;
  --brand-dark:#12307c;
  --sky:#5bb8e0;
  --ink:#222;
  --muted:#444;
  --rule:#cfcfcf;
  --panel:#f4f4f4;
  --panel-border:#dedede;
  --white:#fff;
}
*{box-sizing:border-box;margin:0;padding:0}
html,body{width:967px;height:1200px;overflow:hidden;background:var(--white)}
body{font-family:"Arimo",Arial,sans-serif;color:var(--ink);position:relative}
.page{position:relative;width:967px;height:1200px}
.topline{position:absolute;top:0;left:0;width:100%;height:3px;background:var(--brand)}

.brand{position:absolute;left:112px;top:36px;display:flex;align-items:center;gap:10px}
.brand-mark{width:44px;height:44px;border-radius:50%;background:var(--brand)}
.brand-name{font-size:30px;font-weight:700;color:var(--brand);letter-spacing:-.5px}

.search{position:absolute;left:695px;top:23px;width:160px;height:22px;border:1px solid #cfcfcf;border-radius:11px;background:#fff}
.search span{position:absolute;left:10px;top:4px;font-size:10px;color:#aaa}
.search svg{position:absolute;right:2px;top:2px}

.nav{position:absolute;left:592px;top:58px;width:263px;height:29px;display:flex;border-radius:15px;overflow:hidden;background:var(--brand)}
.nav a{display:flex;align-items:center;justify-content:center;color:#fff;font-size:11px;font-weight:700;text-decoration:none;padding:0 12px;height:100%}
.nav a.active{background:var(--sky);color:var(--brand-dark);width:54px}

.hero{position:absolute;left:0;top:109px;width:967px;height:312px;background:linear-gradient(120deg,#e8902a 0%,#8a8f99 18%,#4a3a4a 35%,#8a9a4a 55%,#6e7480 70%,#b8323a 85%,#8a8e96 100%)}
.hero-caption{position:absolute;left:112px;top:195px;width:743px;height:90px;background:rgba(40,40,40,.72);padding:12px 14px;color:#fff}
.hero-caption h2{font-size:18px;font-weight:700;margin-bottom:8px}
.hero-caption p{font-size:10px;line-height:15px;color:#e4e4e4}
.dots{position:absolute;top:296px;left:454px;display:flex;gap:6px}
.dots i{width:9px;height:9px;border-radius:50%;background:#fff}
.dots i.on{background:var(--sky)}

.welcome{position:absolute;left:112px;top:439px;width:743px}
.welcome h1{text-align:center;font-size:23px;font-weight:400;color:#333}
.welcome h1 b{color:var(--brand);font-weight:700}
.welcome p{margin-top:10px;font-size:10px;line-height:16px;color:var(--ink);text-align:justify}
.rule{position:absolute;left:112px;width:743px;height:1px;background:var(--rule)}

.services-title{position:absolute;left:112px;top:542px;width:743px;text-align:center;font-size:22px;font-weight:700;color:var(--brand)}
.services-sub{position:absolute;left:112px;top:575px;width:743px;text-align:center;font-size:10px;color:var(--muted)}
.card{position:absolute;top:601px;width:162px;height:164px;border:1px solid #d2d2d2;border-radius:4px;background:#fff;text-align:center}
.card .thumb{margin:10px auto 0;width:140px;height:98px;border:1px solid #ccc;border-radius:3px;padding:4px;background:#fff}
.card .thumb div{width:100%;height:100%}
.card h3{font-size:13.5px;font-weight:400;color:#222;margin-top:14px;line-height:15px}
.card.featured{background:var(--brand);border-color:var(--brand)}
.card.featured h3{color:#fff}
.arrow{position:absolute;top:674px}

.panel{position:absolute;top:812px;width:364px;height:244px;background:var(--panel);border:1px solid var(--panel-border);border-radius:3px}
.panel h2{text-align:center;font-size:21px;font-weight:700;color:var(--brand);margin-top:8px}
.category ul{list-style:none;margin:14px 0 0 12px}
.category li{font-size:9.5px;font-weight:700;color:#333;height:21.6px;padding-left:12px;position:relative}
.category li::before{content:"";position:absolute;left:0;top:2px;width:4px;height:4px;border-right:2px solid var(--brand);border-bottom:2px solid var(--brand);transform:rotate(-45deg)}
.category .more{font-size:9.5px;font-weight:700;color:var(--brand);margin-left:24px}
.news-item{margin:8px 12px 0 9px}
.news-item h4{font-size:12px;font-weight:700;color:var(--brand);display:flex;align-items:center;gap:6px}
.news-item p{font-size:9.8px;line-height:15px;color:#222;margin-top:4px;text-align:justify}
.news-sep{height:1px;background:var(--rule);margin:8px 12px 0 9px}
.pager{position:absolute;right:12px;bottom:10px}

.footer{position:absolute;left:0;top:1086px;width:967px;height:114px;background:linear-gradient(#2a52b0,#163b94);border-top:6px solid var(--sky)}
.footer-nav{position:absolute;left:112px;top:33px;display:flex;font-size:10px;font-weight:700;color:#fff}
.footer-nav a{color:#fff;text-decoration:none}
.footer-nav a.active{color:#9fd6f0}
.footer-nav span{margin:0 16px;color:#cfe3ff}
.copy{position:absolute;left:112px;top:76px;font-size:9px;color:#8fc8ee}
.follow{position:absolute;right:112px;top:74px;display:flex;align-items:center;gap:4px;font-size:10px;font-weight:700;color:#fff}
.follow i{width:11px;height:11px;background:#4a90d8;border:1px solid #fff}
.follow i.alt{background:#f08030}
</style>
</head>
<body>
<div class="page">
  <div class="topline"></div>

  <header>
    <div class="brand"><span class="brand-mark"></span><span class="brand-name">Quorvel Enterprises</span></div>
    <div class="search"><span>Search_</span>
      <svg width="18" height="18" viewBox="0 0 18 18"><circle cx="9" cy="9" r="9" fill="#555"/><circle cx="8" cy="8" r="3.5" fill="none" stroke="#fff" stroke-width="1.5"/><line x1="10.5" y1="10.5" x2="13" y2="13" stroke="#fff" stroke-width="1.8"/></svg>
    </div>
    <nav class="nav">
      <a class="active" href="#">Home</a><a href="#">About Us</a><a href="#">Services</a><a href="#">Contact Us</a>
    </nav>
  </header>

  <section class="hero" role="img" aria-label="Fresh fruit on a grey wooden table: orange, grapes, kiwi and strawberries">
    <div class="hero-caption">
      <h2>Lorem ipsum dolor sit amet</h2>
      <p>Consectetuer adipiscing elit, sed diam nonummy nibh euismod tincidunt ut laoreet dolore magna aliquam erat volutpat. Ut wisi enim ad minim veniam, quis nostrud exerci tation ullamcorper suscipit lobortis nisl ut aliquip ex ea commodo consequat.</p>
    </div>
    <div class="dots"><i></i><i></i><i class="on"></i><i></i></div>
  </section>

  <section class="welcome">
    <h1>Welcome to <b>Quorvel Enterprises</b></h1>
    <p>Quorvel Enterprises connects manufacturers, distributors and retailers to satisfy target consumer and retailer needs. We utilize our expertise in, product development, manufacturing, global sourcing and retail to provide exceptional account management, product launch and branding services.</p>
  </section>
  <div class="rule" style="top:526px"></div>

  <h2 class="services-title">Services</h2>
  <p class="services-sub">Quorvel Enterprises connects manufacturers, distributors and retailers to satisfy target consumer and retailer needs.</p>

  <svg class="arrow" style="left:112px" width="16" height="20" viewBox="0 0 16 20"><path d="M12 2 L4 10 L12 18" fill="none" stroke="#c8c8c8" stroke-width="4"/></svg>
  <article class="card" style="left:143px">
    <div class="thumb"><div role="img" aria-label="Desk with calculator, charts and coffee cup" style="background:linear-gradient(135deg,#d8d8d8,#8a8a8a)"></div></div>
    <h3>Account Management</h3>
  </article>
  <article class="card featured" style="left:317px">
    <div class="thumb"><div role="img" aria-label="Gears with small figures pushing them" style="background:linear-gradient(135deg,#f0f0f0,#666)"></div></div>
    <h3>Product Development</h3>
  </article>
  <article class="card" style="left:491px">
    <div class="thumb"><div role="img" aria-label="Sphere covered in branding words" style="background:radial-gradient(circle,#e8eef4,#fff)"></div></div>
    <h3>Brand Development &amp; Brand Management</h3>
  </article>
  <article class="card" style="left:664px">
    <div class="thumb"><div role="img" aria-label="Green blocks on a grey plain under a cloudy sky" style="background:linear-gradient(#9aa8b8,#6a7068)"></div></div>
    <h3>Sourcing</h3>
  </article>
  <svg class="arrow" style="left:839px" width="16" height="20" viewBox="0 0 16 20"><path d="M4 2 L12 10 L4 18" fill="none" stroke="var(--brand)" stroke-width="4"/></svg>

  <div class="rule" style="top:789px"></div>

  <section class="panel category" style="left:111px">
    <h2>Category</h2>
    <ul>
      <li>Lorem ipsum dolor</li>
      <li>hendrerit in vulputate velit</li>
      <li>exerci tation ullamcorperel eum iriure</li>
      <li>consectetuer adipiscing elit</li>
      <li>Duis autem vel eum iriure ullamcorper</li>
      <li>exerci tation ullamcorper</li>
      <li>Lorem ipsum dolor el eum iriure</li>
      <li>hendrerit in vulputate velit</li>
    </ul>
    <div class="more">View all</div>
  </section>

  <section class="panel news" style="left:491px">
    <h2>News &amp; Updates</h2>
    <div class="news-item">
      <h4><svg width="14" height="14" viewBox="0 0 14 14"><rect x="1" y="2" width="12" height="11" fill="none" stroke="#555"/><rect x="1" y="2" width="12" height="3" fill="#555"/><path d="M3 7h2M6 7h2M9 7h2M3 10h2M6 10h2M9 10h2" stroke="#555"/></svg>Consectetuer adipiscing elit</h4>
      <p>Lorem ipsum dolor sit amet, consectetuer adipiscing elit, sed diam nonummy nibh euismod tincidunt ut laoreet dolore magna aliquam erat.quis nostrud exerci tation ullamcorper suscipit lobortis nisl ut aliquip ex ea commodo consequat. Duis autem.</p>
    </div>
    <div class="news-sep"></div>
    <div class="news-item">
      <h4><svg width="14" height="14" viewBox="0 0 14 14"><rect x="1" y="2" width="12" height="11" fill="none" stroke="#555"/><rect x="1" y="2" width="12" height="3" fill="#555"/><path d="M3 7h2M6 7h2M9 7h2M3 10h2M6 10h2M9 10h2" stroke="#555"/></svg>Consectetuer adipiscing elit</h4>
      <p>Lorem ipsum dolor sit amet, consectetuer adipiscing elit, sed diam nonummy nibh euismod tincidunt ut laoreet dolore magna aliquam erat.quis nostrud exerci tation ullamcorper suscipit lobortis nisl ut aliquip ex ea commodo consequat. Duis autem.</p>
    </div>
    <svg class="pager" width="26" height="12" viewBox="0 0 26 12"><path d="M8 1 L3 6 L8 11" fill="none" stroke="#aaa" stroke-width="2.5"/><path d="M18 1 L23 6 L18 11" fill="none" stroke="#aaa" stroke-width="2.5"/></svg>
  </section>

  <footer class="footer">
    <nav class="footer-nav"><a class="active" href="#">Home</a><span>|</span><a href="#">About Us</a><span>|</span><a href="#">Services</a><span>|</span><a href="#">Contact us</a></nav>
    <p class="copy">Copyright © 2014 Quorvel Enterprises.All Rights Reserved</p>
    <div class="follow">Follow us on: <i></i><i></i><i></i><i class="alt"></i></div>
  </footer>
</div>
</body>
</html>
```